IT Services

We come to you
Only $49/hr
No contract, no monthly fee
Software engineer on staff
remote assistance or visit in your office

On the back of the card I want to list services.

- Server setup
- Network troubleshooting
- Printer setup
- Secure backup setup
- Software installation
- Wireless network setup
- Wired network setup
- Disaster recovery
- Website management
- Any other technology related support
- Email setup
- HIPAA compliance review and setup
Updates

the URL is: BYTEHARBOR.ZONE please use it on the card

On the card we need to mention "Connect remotely to address your IT issues" if there is enough room as well as "we go to you"

Industry/Entity Type

Printer

Contact Information for Business Card

I want a busoiness card to offer my services to doctor offices, it can be dentists, Otamatry, and other professions. I provide the following service. My plan is to go to their office and drop off my card. I don't want them to forget about it that is why I am paying for the design. I like hand writing design formats.

```html
<!DOCTYPE html>
<html lang="en">
<head>
<meta charset="utf-8">
<title>ByteHarbor IT Services – Business Card</title>
<link rel="stylesheet" href="https://fonts.googleapis.com/css2?family=Architects+Daughter&family=Indie+Flower&display=swap">
<style>
  :root {
    --backdrop: #2b2b2b;
    --card-top: #ffffff;
    --card-bottom: #d9d9d9;
    --ink: #161616;
    --ink-soft: #6f6f6f;
    --sketch-light: #eeeeee;
    --sketch-mid: #cfcfcf;
  }
  * { box-sizing: border-box; margin: 0; padding: 0; }
  html, body {
    width: 1200px;
    height: 900px;
    overflow: hidden;
    background: var(--backdrop);
  }
  .canvas {
    width: 1200px;
    height: 900px;
    display: flex;
    align-items: center;
    justify-content: center;
    gap: 40px;
  }
  .card {
    position: relative;
    width: 540px;
    height: 310px;
    border-radius: 18px;
    background: linear-gradient(160deg, var(--card-top) 0%, var(--card-top) 45%, var(--card-bottom) 100%);
    box-shadow: 0 10px 30px rgba(0, 0, 0, 0.5);
    overflow: hidden;
  }
  .web-address {
    position: absolute;
    font-family: "Architects Daughter", cursive;
    font-size: 32px;
    letter-spacing: 2px;
    color: var(--ink);
    white-space: nowrap;
  }
  .web-address .domain-end { color: var(--ink-soft); }

  /* Front */
  .offer {
    position: absolute;
    left: 28px;
    top: 120px;
    width: 200px;
    font-family: "Indie Flower", cursive;
    font-size: 17px;
    line-height: 1.25;
    text-align: center;
    color: var(--ink);
  }
  .network-sketch {
    position: absolute;
    left: 235px;
    top: 22px;
    width: 285px;
    height: 195px;
    border-radius: 10px;
    background: radial-gradient(ellipse at center, var(--sketch-mid) 0%, var(--sketch-light) 70%, transparent 100%);
  }
  .card-front .web-address { left: 30px; bottom: 22px; }

  /* Back */
  .services {
    position: absolute;
    left: 30px;
    right: 30px;
    top: 48px;
    list-style: none;
    font-family: "Indie Flower", cursive;
    font-size: 20px;
    line-height: 1.3;
    text-align: center;
    color: var(--ink-soft);
  }
  .card-back .web-address { left: 60px; bottom: 24px; }
</style>
</head>
<body>
<main class="canvas">
  <section class="card card-front">
    <p class="offer">
      We come to you<br>
      Only $49/hr<br>
      No contract, no monthly fee<br>
      Software engineer on staff<br>
      remote assistance or visit in your office
    </p>
    <div class="network-sketch" role="img" aria-label="Hand-drawn sketch of an office network: internet cloud, firewall, router, server, laptop, desktop, printer and mobile phone joined by arrows"></div>
    <p class="web-address">WWW.BYTEHARBOR<span class="domain-end">.ZONE</span></p>
  </section>

  <section class="card card-back">
    <ul class="services">
      <li>◦ Server setup &nbsp;◦ Network troubleshooting</li>
      <li>◦ Printer setup &nbsp;◦ Secure backup setup</li>
      <li>◦ Software installation &nbsp;◦ Wireless network setup</li>
      <li>◦ Wired network setup &nbsp;◦ Disaster recovery</li>
      <li>◦ Website management &nbsp;◦ Any other technology</li>
      <li>related support &nbsp;◦ Email setup</li>
      <li>◦ HIPAA compliance review and setup</li>
    </ul>
    <p class="web-address">WWW.BYTEHARBOR<span class="domain-end">.ZONE</span></p>
  </section>
</main>
</body>
</html>
```